Invitation - Photos with Santa

We’re doing an event this Christmas for people get photos with Santa.
It’ll be a postcard that we mail to people we know.
Size: 5 x 7, two sided
Details for back of postcard:
Saturday, December 4
10 a.m. - 12 p.m.
18457 Colvin Ln.
Strongsville, OH 44873
The company putting it on is Brightwick. I’ve got a million logo formats so just let me know what you need.
In terms of theme/look/feel for the front of card, I’m a little stuck so I’m open to whatever.
-Skip the line?
-Private Santa party?
-Screw the mall?
Attached is an old one we used last time time we did it.
Let me know if there are any questions!
People I know personally, people with kids, people who private photo with Santa without having to go to the mall

```html
<!DOCTYPE html>
<html lang="en">
<head>
<meta charset="utf-8">
<title>Brightwick – A Barking Christmas Party</title>
<link href="https://fonts.googleapis.com/css2?family=Lobster&family=Montserrat:wght@500;600&family=Raleway:wght@400;500&family=Yellowtail&display=swap" rel="stylesheet">
<style>
  :root {
    --page: #e8e8e8;
    --pine: #1b7a3a;
    --pine-deep: #0f5a26;
    --pine-band: #135e28;
    --cream-yellow: #eeee8e;
    --wine: #7a1a1e;
    --berry: #d4141c;
    --flame: #e2421f;
    --ink: #3d3d3d;
    --rule: #555555;
    --white: #ffffff;
  }
  * { margin: 0; padding: 0; box-sizing: border-box; }
  html, body {
    width: 1200px; height: 456px; overflow: hidden;
    background: var(--page);
  }
  .canvas { position: relative; width: 1200px; height: 456px; }

  .card { position: absolute; top: 35px; width: 540px; height: 385px; overflow: hidden; }

  /* Front */
  .card--front { left: 34px; }
  .front-photo {
    position: absolute; inset: 0;
    background:
      radial-gradient(ellipse 38% 55% at 50% 55%, #c9a67a 0%, #b58e62 45%, rgba(27,122,58,0) 75%),
      linear-gradient(160deg, var(--pine) 0%, var(--pine-deep) 100%);
  }
  .brand {
    position: absolute; display: flex; align-items: center; gap: 5px;
    font-family: "Montserrat", sans-serif; font-weight: 600;
    color: var(--flame); letter-spacing: 0.2px; line-height: 1;
  }
  .brand__dot { border-radius: 50%; background: var(--flame); }
  .brand--front { left: 28px; top: 38px; font-size: 16px; }
  .brand--front .brand__dot { width: 17px; height: 17px; }

  .headline {
    position: absolute; left: 72px; width: 393px; top: 214px;
    text-align: center; white-space: nowrap;
    font-family: "Yellowtail", "Lobster", cursive; color: var(--cream-yellow);
    font-size: 108px; line-height: 1;
  }
  .headline-sub {
    position: absolute; left: 200px; width: 140px; top: 322px;
    text-align: center; white-space: nowrap;
    font-family: "Lobster", cursive; color: var(--wine);
    font-size: 40px; line-height: 1;
  }

  /* Back */
  .card--back { left: 626px; background: var(--white); }
  .band {
    position: absolute; left: 0; top: 0; width: 100%; height: 79px;
    background: linear-gradient(90deg, var(--pine-band), #17692f 60%, var(--pine-band));
    color: var(--white); text-align: center;
    font-family: "Montserrat", sans-serif; font-weight: 600;
    font-size: 13px; letter-spacing: 3.8px; line-height: 14px;
    padding-top: 27px; padding-left: 10px;
  }
  .details {
    position: absolute; left: 0; top: 79px; width: 269px; text-align: center;
  }
  .details__kicker {
    position: absolute; left: 0; width: 100%; top: 22px;
    font-family: "Raleway", sans-serif; font-size: 10px;
    letter-spacing: 2.6px; color: var(--ink);
  }
  .details__when {
    position: absolute; left: 0; width: 100%; top: 70px;
    font-family: "Raleway", sans-serif; font-size: 18px; line-height: 26px;
    color: var(--ink);
  }
  .details__for {
    position: absolute; left: 0; width: 100%; top: 153px;
    font-family: "Raleway", sans-serif; font-size: 10px;
    letter-spacing: 3px; color: var(--berry);
  }
  .details__pitch {
    position: absolute; left: -8px; width: 285px; top: 166px;
    font-family: "Lobster", cursive; color: var(--berry);
    font-size: 20px; line-height: 26px; white-space: nowrap;
  }
  .details__pitch .line-2 { font-size: 23px; }
  .details__address {
    position: absolute; left: 0; width: 100%; top: 272px;
    font-family: "Raleway", sans-serif; font-size: 12px; color: var(--ink);
    white-space: nowrap;
  }
  .divider {
    position: absolute; left: 269px; top: 97px; width: 1.5px; height: 271px;
    background: var(--rule);
  }
  .brand--back { left: 362px; top: 354px; font-size: 11px; }
  .brand--back .brand__dot { width: 12px; height: 12px; }

  .overflow-note {
    position: absolute; left: 1164px; top: 56px;
    font-family: "Raleway", sans-serif; font-size: 14px; color: var(--berry);
    transform: rotate(8deg); white-space: nowrap;
  }
</style>
</head>
<body>
<main class="canvas">
  <section class="card card--front">
    <div class="front-photo" role="img" aria-label="Photo of a small shaggy dog dressed as a Christmas elf on a green backdrop"></div>
    <div class="brand brand--front"><span class="brand__dot"></span>BRIGHTWICK</div>
    <p class="headline">celebrate</p>
    <p class="headline-sub">with us</p>
  </section>

  <section class="card card--back">
    <header class="band">THE WILD DOGS AT BRIGHTWICK<br>INVITE YOU TO</header>
    <div class="details">
      <p class="details__kicker">A BARKING CHRISTMAS PARTY!</p>
      <p class="details__when">Saturday, December 4<br>10am - 12pm</p>
      <p class="details__for">FOR</p>
      <p class="details__pitch">some puppy love<br><span class="line-2">and your photo with santa</span></p>
      <p class="details__address">18457 Colvin Ln, Strongville OH44873</p>
    </div>
    <div class="divider"></div>
    <div class="brand brand--back"><span class="brand__dot"></span>BRIGHTWICK</div>
  </section>

  <span class="overflow-note">t your</span>
</main>
</body>
</html>
```